Business Cards and Letterhead for Solo Attorney
Mark Whitfield, Esq., APC
Business Cards and Letterhead for Solo Attorney - Law
Creative Brief
Professional
SEE ADDITIONAL COMMENTS BELOW
742 S. Milbrook Avenue West Covina, CA 91790
mark@whitfieldlegal.example
NAME/TITLE SHOULD APPEAR AS FOLLOWS: Mark Whitfield Attorney at Law Civil Litigation Counsel It should also have my corporate name somewhere: Mark Whitfield, Esq., APC

```html
<!DOCTYPE html>
<html lang="en">
<head>
<meta charset="UTF-8">
<title>Mark Whitfield, Esq., APC — Business Card</title>
<link rel="stylesheet" href="https://fonts.googleapis.com/css2?family=Oswald:wght@600&family=Open+Sans:wght@400;600&display=swap">
<style>
  :root {
    --backdrop: #e9e7e3;
    --card-white: #ffffff;
    --brand-blue: #1f3ea8;
    --brand-blue-deep: #16308c;
    --accent-gold: #c9a35a;
    --text-dark: #3a3a3a;
    --rule: #d9d9d9;
  }
  * { box-sizing: border-box; margin: 0; padding: 0; }
  html, body { width: 1200px; height: 794px; overflow: hidden; }
  body {
    background: var(--backdrop);
    font-family: "Open Sans", sans-serif;
    display: flex;
    align-items: center;
    justify-content: center;
    gap: 60px;
  }
  .card {
    width: 500px;
    height: 286px;
    border-radius: 10px;
    position: relative;
    overflow: hidden;
    box-shadow: 0 6px 18px rgba(0,0,0,0.18);
  }

  /* Front */
  .card-front { background: var(--card-white); display: flex; }
  .front-brand {
    width: 210px;
    display: flex;
    flex-direction: column;
    align-items: center;
    justify-content: center;
    gap: 14px;
    padding: 0 18px 24px;
  }
  .brand-square { width: 34px; height: 34px; background: var(--brand-blue); }
  .brand-name {
    font-family: "Oswald", sans-serif;
    font-weight: 600;
    font-size: 19px;
    letter-spacing: 0.5px;
    color: var(--brand-blue);
    text-transform: uppercase;
    text-align: center;
    line-height: 1.15;
  }
  .front-divider { width: 1px; background: var(--rule); margin: 30px 0 50px; }
  .front-details { flex: 1; padding: 34px 24px 40px 26px; }
  .person-name { font-size: 17px; font-weight: 600; color: var(--brand-blue); }
  .person-titles { margin-top: 4px; font-size: 10.5px; line-height: 1.45; color: var(--accent-gold); }
  .contact-list { list-style: none; margin-top: 16px; font-size: 10.5px; color: var(--text-dark); }
  .contact-list li { display: flex; align-items: flex-start; gap: 8px; margin-bottom: 6px; line-height: 1.4; }
  .contact-list svg { width: 11px; height: 11px; flex: none; margin-top: 2px; fill: var(--brand-blue); }
  .front-web {
    position: absolute; left: 0; right: 0; bottom: 10px;
    height: 22px; display: flex; align-items: center; justify-content: flex-end;
    padding-right: 24px; font-size: 10.5px; letter-spacing: 1px; color: var(--brand-blue);
  }
  .front-band { position: absolute; left: 0; right: 0; bottom: 0; height: 8px; background: var(--brand-blue); }

  /* Back */
  .card-back {
    background: linear-gradient(135deg, var(--brand-blue) 0%, var(--brand-blue-deep) 100%);
  }
  .back-text { position: absolute; right: 28px; bottom: 26px; text-align: right; color: var(--card-white); }
  .back-name {
    font-family: "Oswald", sans-serif; font-weight: 600; font-size: 20px;
    letter-spacing: 0.6px; text-transform: uppercase;
  }
  .back-web { margin-top: 2px; font-size: 10.5px; letter-spacing: 1.5px; opacity: 0.9; }
</style>
</head>
<body>
  <section class="card card-front" aria-label="Business card front">
    <div class="front-brand">
      <div class="brand-square"></div>
      <div class="brand-name">Mark Whitfield Esq., APC</div>
    </div>
    <div class="front-divider"></div>
    <div class="front-details">
      <div class="person-name">Mark Whitfield</div>
      <div class="person-titles">Attorney at Law<br>Civil Litigation Counsel</div>
      <ul class="contact-list">
        <li>
          <svg viewBox="0 0 12 12"><path d="M6 0a4 4 0 0 0-4 4c0 3 4 8 4 8s4-5 4-8a4 4 0 0 0-4-4zm0 5.5A1.5 1.5 0 1 1 6 2.5a1.5 1.5 0 0 1 0 3z"/></svg>
          <span>742 S. Milbrook Avenue<br>Fairhaven, CA 95012</span>
        </li>
        <li>
          <svg viewBox="0 0 12 12"><path d="M2.5 0.5l2 2.5-1 1.5c.7 1.5 2 2.8 3.5 3.5l1.5-1 2.5 2-1 2.5C5 11 1 7 0.5 1.5z"/></svg>
          <span>(555) 201-0148</span>
        </li>
        <li>
          <svg viewBox="0 0 12 12"><path d="M3 0h6v3H3zM1 4h10v5H9v3H3V9H1zm3 4v3h4V8z"/></svg>
          <span>(555) 201-0192</span>
        </li>
        <li>
          <svg viewBox="0 0 12 12"><path d="M0 2h12v8H0zm1 1v.5l5 3.5 5-3.5V3z"/></svg>
          <span>mark@whitfieldlegal.example</span>
        </li>
      </ul>
    </div>
    <div class="front-web">www.whitfieldlegal.example</div>
    <div class="front-band"></div>
  </section>

  <section class="card card-back" aria-label="Business card back">
    <div class="back-text">
      <div class="back-name">Mark Whitfield Esq., APC</div>
      <div class="back-web">www.whitfieldlegal.example</div>
    </div>
  </section>
</body>
</html>
```